Product configurator design for a loudspeaker manufacturing company

The task is to create a design for an online product configurator, where customers are able to design and configure their own loudspeakers in a simple, elegant and playful way. Please have a look at the given sketches that demonstrate the essential elements and functions. The 3d model and the selection menu on the right side are the most important elements for this configurator. Please use a decent color scheme because the loudspeaker and the selection menu already include many colors. page 1: configurator (focus on that page) page 2: landing page Additional ideas: -The landing page is allowed to become a more colorful color scheme in contrast to the configurator page. -The theme of the landing page could be individuality and diversity.

Target Market(s)

germany

Industry/Entity Type

Manufacturing

Coding

Coded - Design and coding required

Number of Pages Required

2 page

Font styles to use
Serif
Sans Serif

Colors

Designer to choose colors to be used in the design.

Requirements
Must have
• - functional html-site - useable selection menu - design navigation bar
Nice to have
• - suggestions for enhanced user-experience -

```html
<!DOCTYPE html>
<html lang="en">
<head>
<meta charset="utf-8">
<title>Voltra – Configurator</title>
<link href="https://fonts.googleapis.com/css2?family=Poppins:wght@300;400;500;600;700&display=swap" rel="stylesheet">
<style>
:root{
  --red:#d3303f;
  --red-light:#e04458;
  --ink:#222;
  --text:#444;
  --line:#dcdcdc;
  --page:#f4f4f4;
  --white:#fff;
  --footer:#2a2f3b;
  --footer-text:#e6e6e6;
}
*{box-sizing:border-box;margin:0;padding:0}
html,body{width:822px;height:1200px;overflow:hidden}
body{font-family:'Poppins',sans-serif;color:var(--text);background:var(--page);position:relative}
.abs{position:absolute}
.header{left:0;top:0;width:822px;height:66px;background:var(--white);border-bottom:1px solid #d8d8d8;box-shadow:0 1px 3px rgba(0,0,0,.08)}
.logo{left:90px;top:12px;font-size:29px;font-weight:600;color:#111;letter-spacing:-.5px}
.nav{left:0;top:0;height:66px;width:822px}
.nav a{position:absolute;top:27px;font-size:10px;font-weight:500;color:#222;text-decoration:none}
.nav .active{top:20px;left:525px;width:96px;height:26px;line-height:26px;text-align:center;background:var(--red);color:#fff;border-radius:13px}
.fav-title{left:90px;top:106px;font-size:14px;font-weight:500;color:#222}
.thumbs{left:90px;top:130px;width:62px;height:205px;background:#fff;border:1px solid #e4e4e4}
.thumb{height:50px;margin:1px;border-bottom:1px solid #eee}
.thumb div{width:52px;height:36px;margin:6px auto;border-radius:4px}
.scroll{left:154px;top:130px;width:4px;height:200px;background:#222;border-radius:2px}
.scroll span{position:absolute;left:-1px;top:4px;width:6px;height:18px;background:#555;border-radius:3px}
.tabs{left:179px;top:112px;width:284px;height:29px;display:flex}
.tabs div{flex:1;text-align:center;line-height:29px;font-size:12px;color:#fff}
.tab-render{background:#111}
.tab-model{background:var(--red)}
.viewer{left:179px;top:149px;width:284px;height:187px;background:linear-gradient(180deg,#f2f2f2,#fafafa);border:1px solid #e2e2e2;box-shadow:0 1px 3px rgba(0,0,0,.1)}
.product{left:33px;top:28px;width:220px;height:130px;border-radius:28px;background:linear-gradient(135deg,#9d958c,#7b736b 60%,#b0a89f)}
.arrow{width:18px;height:26px;background:#fff;border:1px solid #ddd;font-size:10px;text-align:center;line-height:24px;color:#333}
.shares{left:182px;top:361px;display:flex;gap:6px}
.dot{width:22px;height:22px;border-radius:50%}
.steps{left:484px;top:112px;width:247px}
.step{height:34px;margin-bottom:4px;background:#fff;border:1px solid #ddd;font-size:9px;color:#333;padding:0 10px;display:flex;align-items:center;justify-content:space-between}
.specs{left:90px;top:408px;width:641px;border-collapse:collapse;background:#fff;font-size:9px;color:#333;box-shadow:0 1px 3px rgba(0,0,0,.1)}
.specs td{border:1px solid var(--line);padding:0 12px;height:36px}
.specs tr:last-child td{height:44px}
.shop-btn{display:inline-block;background:var(--red);color:#fff;font-size:10px;font-weight:500;padding:0 11px;height:25px;line-height:25px;border-radius:13px;margin-left:85px}
.desc-head{left:90px;top:563px;width:640px;height:32px;background:linear-gradient(90deg,var(--red-light),var(--red) 60%,#bf2a38);color:#fff;font-size:14px;padding:0 15px;line-height:32px}
.desc-body{left:90px;top:595px;width:640px;height:248px;background:#fff;border:1px solid #e6e6e6;padding:22px 20px 0}
.desc-body h2{font-size:13px;font-weight:600;color:#333;margin-bottom:8px}
.desc-body p{font-size:7.4px;line-height:15.3px;color:#333;margin-bottom:8px;width:560px}
.desc-body li{list-style:none;font-size:7.6px;line-height:15.2px;color:#333;padding-left:13px;position:relative}
.desc-body li:before{content:"";position:absolute;left:0;top:4px;width:6px;height:6px;border-radius:50%;background:#666}
.footer{left:0;top:896px;width:822px;height:304px;background:var(--footer);color:var(--footer-text)}
.footer h3{position:absolute;color:#fff;font-weight:600}
.footer p{position:absolute;font-size:7.8px;line-height:15.3px}
.ring{width:21px;height:21px;border-radius:50%;border:1px solid #ccc}
.email{left:534px;top:123px;width:196px;height:24px;background:#fff;border-radius:12px;font-size:7px;color:#555;line-height:24px;padding-left:11px}
.email span{position:absolute;right:0;top:0;height:24px;width:70px;background:var(--red);color:#fff;border-radius:12px;text-align:center;font-size:8px;font-weight:600}
.bottom{left:0;top:236px;width:822px;border-top:1px solid #454b57}
.card{width:27px;height:16px;background:#fff;border-radius:2px;font-size:5px;font-weight:600;color:#333;text-align:center;line-height:16px}
</style>
</head>
<body>
<header class="header abs">
  <div class="logo abs">VOLTRA</div>
  <nav class="nav abs">
    <a style="left:415px">HOME</a>
    <a style="left:468px">PRODUCT</a>
    <a class="active">CONFIGURATOR</a>
    <a style="left:635px">TEAM</a>
    <a style="left:686px">CONTACT</a>
  </nav>
</header>

<div class="fav-title abs">Favorites</div>
<div class="thumbs abs">
  <div class="thumb"><div role="img" aria-label="Saved speaker design, stone finish" style="background:#a39b93"></div></div>
  <div class="thumb"><div role="img" aria-label="Saved speaker pair, dark wood" style="background:#5a514b"></div></div>
  <div class="thumb"><div role="img" aria-label="Saved speaker array" style="background:#6d6d6d"></div></div>
  <div class="thumb" style="border:0"><div role="img" aria-label="Saved speaker set" style="background:#555"></div></div>
</div>
<div class="scroll abs"><span></span></div>

<div class="tabs abs"><div class="tab-render">Rendering</div><div class="tab-model">3D-Model</div></div>
<div class="viewer abs">
  <div class="product abs" role="img" aria-label="Rendered loudspeaker with stone-look body and white rounded sides"></div>
  <svg class="abs" style="left:9px;top:12px" width="22" height="20" viewBox="0 0 24 22"><path d="M12 21 2 11C-1 7 1 1 6 1c3 0 5 2 6 4 1-2 3-4 6-4 5 0 7 6 4 10z" fill="var(--red)"/></svg>
  <div class="arrow abs" style="left:8px;top:86px">‹</div>
  <div class="arrow abs" style="left:260px;top:86px">›</div>
</div>

<div class="shares abs">
  <div class="dot" style="background:#2f4f9a"></div>
  <div class="dot" style="background:#4caf50"></div>
  <div class="dot" style="background:#d3262e"></div>
  <div class="dot" style="background:#3aa84a"></div>
  <div class="dot" style="background:#d43a7a"></div>
</div>
<svg class="abs" style="left:419px;top:362px" width="46" height="21">
  <circle cx="10.5" cy="10.5" r="10.5" fill="#111"/><path d="M10 6v9l-5-4.5zM15 6v9l-5-4.5z" fill="#fff"/>
  <circle cx="35.5" cy="10.5" r="10.5" fill="var(--red)"/><path d="M31 6v9l5-4.5zM36 6v9l5-4.5z" fill="#fff"/>
</svg>

<div class="steps abs">
  <div class="step">1. Model<span>⌄</span></div>
  <div class="step">2. Size<span>⌄</span></div>
  <div class="step">3. Body<span>⌄</span></div>
  <div class="step">4. Sides<span>⌄</span></div>
  <div class="step">5. Chassis<span>⌄</span></div>
  <div class="step">6. Feet<span>⌄</span></div>
</div>

<table class="specs abs">
  <tr><td style="width:98px">Frequency range</td><td style="width:60px">5 - 30k</td><td style="width:149px">Dimensions H, W, D in mm</td><td style="width:104px;text-align:center">123 x 231 x 123</td><td style="width:121px">Total price</td><td style="text-align:center">1429,- €</td></tr>
  <tr><td>Max sound level</td><td>120 db</td><td>Weight in Kg</td><td>5,6</td><td>Delivery time</td><td style="text-align:center">6 Tage</td></tr>
  <tr><td>Power</td><td>50</td><td></td><td></td><td colspan="2" style="padding:0"><span class="shop-btn">To Marketplace</span></td></tr>
</table>

<div class="desc-head abs">Product description<span style="float:right;font-size:11px">⌄</span></div>
<div class="desc-body abs">
  <h2>QUIS AUTEM VEL EUM IURE REPREHENDERIT QUI</h2>
  <p>Lorem ipsum dolor sit amet, consectetur adipiscing elit, sed do eiusmod tempor incididunt ut labore et dolore magna aliqua. Ut enim ad minim veniam, quis nostrud exercitation ullamco laboris nisi ut aliquip ex ea commodo consequat. Duis aute irure dolor in reprehenderit in voluptate velit esse cillum dolore eu fugiat nulla pariatur. Excepteur sint occaecat cupidatat non proident, sunt in culpa qui officia deserunt mollit anim id est laborum</p>
  <p>Sed ut perspiciatis unde omnis iste natus error sit voluptatem accusantium doloremque laudantium, totam rem aperiam, eaque ipsa quae ab illo inventore veritatis et quasi architecto beatae vitae dicta sunt explicabo. Nemo enim ipsam voluptatem quia voluptas sit aspernatur aut odit aut fugit, sed quia consequuntur magni dolores eos qui ratione voluptatem sequi nesciunt. Neque porro quisquam est,</p>
  <ul>
    <li>Nemo enim ipsam voluptatem</li>
    <li>Ut enim ad minima veniam, quis nostrum</li>
    <li>Quis autem vel eum iure reprehenderit qui</li>
    <li>Duis aute irure dolor in reprehenderit</li>
  </ul>
</div>

<footer class="footer abs">
  <h3 style="left:90px;top:44px;font-size:19px">ABOUT VOLTRA</h3>
  <p style="left:90px;top:83px;width:215px">Sed ut perspiciatis unde omnis iste natus error sit voluptatem accusantium doloremque laudantium, totam rem aperiam, eaque ipsa quae ab illo inventore veritatis et quasi architecto beatae vitae dicta sunt explicabo</p>
  <div class="abs" style="left:90px;top:160px;display:flex;gap:4px"><div class="ring"></div><div class="ring"></div><div class="ring"></div><div class="ring"></div></div>

  <h3 style="left:350px;top:50px;font-size:13px">CONTACT US</h3>
  <svg class="abs" style="left:351px;top:92px" width="8" height="11" viewBox="0 0 8 11"><path d="M4 0a4 4 0 0 0-4 4c0 3 4 7 4 7s4-4 4-7a4 4 0 0 0-4-4zm0 5.5A1.5 1.5 0 1 1 4 2.5a1.5 1.5 0 0 1 0 3z" fill="#fff"/></svg>
  <p style="left:367px;top:87px;font-size:8px;line-height:12.5px">Voltra<br>2140 Harbor Lane Westfield<br>FL 33021</p>
  <svg class="abs" style="left:351px;top:140px" width="9" height="9" viewBox="0 0 10 10"><path d="M2 0l2 2-1 2c1 2 2 3 3 3l2-1 2 2-1 2C4 10 0 6 0 1z" fill="#fff"/></svg>
  <p style="left:368px;top:136px;font-size:8.5px">Phone : 555 018 2749</p>
  <svg class="abs" style="left:351px;top:166px" width="10" height="8" viewBox="0 0 10 8"><path d="M0 0h10v8H0z" fill="#fff"/><path d="M0 0l5 4 5-4" stroke="#2a2f3b" fill="none"/></svg>
  <p style="left:369px;top:162px;font-size:8.5px">Email : hello@voltra-audio.com</p>

  <h3 style="left:535px;top:49px;font-size:12.5px">SIGN UP TO RECEIVE EMAIL</h3>
  <p style="left:535px;top:84px;width:200px;font-size:8px;line-height:12.5px">Excepteur sint occaecat cupidatat non proident, sunt in culpa qui Nemo enim ipsam voluptatem</p>
  <div class="email abs">Enter Email<span>SUBSCRIBE</span></div>
  <div class="abs" style="left:537px;top:166px;display:flex;gap:2px"><div class="ring"></div><div class="ring"></div><div class="ring"></div><div class="ring"></div></div>

  <div class="bottom abs"></div>
  <p style="left:92px;top:258px;font-size:7.6px">© Copyright 2018 Voltra. All Rights Reserved.</p>
  <div class="abs" style="left:610px;top:257px;display:flex;gap:4px">
    <div class="card">CARDO</div><div class="card">PAYRA</div><div class="card">TAPIX</div><div class="card">WALLO</div>
  </div>
</footer>
</body>
</html>
```